Cannabis Security Company- Sales Flyer

Take the copy and make a sleek design- no cannabis leave or paraphernalia. Add graphic elements to the Product Offering section

```html
<!DOCTYPE html>
<html lang="en">
<head>
<meta charset="UTF-8">
<title>Vaultline – Surveillance and IT Hardware Flyer</title>
<link rel="stylesheet" href="https://fonts.googleapis.com/css2?family=Lato:wght@400;700&family=Montserrat:wght@400;900&family=Oswald:wght@600&family=Roboto:wght@400;500;700&display=swap">
<style>
  :root{
    --page-bg:#3b3c3e;
    --paper:#ffffff;
    --sky:#4fb3ea;
    --ink:#1d1d1f;
    --body:#2a2a2a;
    --accent:#0f6fc9;
    --heading-blue:#1f7cc2;
    --band-grey:#ececec;
    --bar-dark:#232323;
    --pill:#16263a;
    --footer-blue:#0f6fd4;
  }
  *{margin:0;padding:0;box-sizing:border-box}
  html,body{width:1200px;height:1200px;overflow:hidden;background:var(--page-bg)}
  .flyer{position:absolute;left:197px;top:30px;width:806px;height:1140px;background:var(--paper);
    font-family:"Lato",sans-serif;color:var(--body);box-shadow:0 10px 30px rgba(0,0,0,.45)}
  .tagline{position:absolute;left:44px;top:41px;height:39px;background:var(--sky);
    font-family:"Montserrat",sans-serif;font-size:24px;color:#fff;line-height:39px;padding:0 12px;white-space:nowrap}
  .tagline strong{font-weight:900;color:var(--ink)}
  .subhead{position:absolute;left:46px;top:88px;font-family:"Oswald",sans-serif;font-weight:600;
    font-size:27px;color:var(--ink);letter-spacing:.2px;white-space:nowrap;transform:scaleX(.88);transform-origin:left}
  .brand-name{position:absolute;left:543px;top:48px;width:240px;display:flex;align-items:center;gap:10px;
    font-family:"Roboto",sans-serif;font-weight:700;font-size:40px;color:var(--ink);letter-spacing:1px}
  .brand-name .mark{width:14px;height:14px;background:var(--ink);flex:none}
  .hero{position:absolute;left:0;top:154px;width:806px;height:370px}
  .intro{position:absolute;left:0;top:524px;width:806px;height:121px;background:var(--band-grey);
    padding:28px 44px 0 49px;font-size:15.2px;line-height:18px;text-align:justify;color:var(--body)}
  .features{position:absolute;top:667px;font-size:14.6px;line-height:18px}
  .features.left{left:49px;width:326px}
  .features.right{left:400px;width:350px}
  .feature{display:flex;gap:11px;margin-bottom:17px}
  .feature .icon{flex:none;width:22px;height:22px;margin-top:-1px}
  .feature p{text-align:justify}
  .feature b{font-weight:400;color:var(--accent)}
  .options{list-style:none;margin:-6px 0 0 25px;font-size:13px;line-height:16px}
  .options li{position:relative;padding-left:13px;margin-bottom:9px;text-align:justify}
  .options li::before{content:"";position:absolute;left:0;top:5px;width:6px;height:6px;border-radius:50%;background:var(--ink)}
  .offering-title{position:absolute;left:0;top:902px;width:806px;text-align:center;font-family:"Roboto",sans-serif;
    font-weight:500;font-size:22px;color:var(--heading-blue)}
  .offering-bar{position:absolute;left:0;top:945px;width:806px;height:67px;background:var(--bar-dark);
    display:flex;align-items:center;font-family:"Roboto",sans-serif;font-weight:500;font-size:16.5px;color:#fff}
  .offering-bar span{height:46px;display:flex;align-items:center;justify-content:center;border-right:1.5px solid #e5e5e5}
  .offering-bar span:last-child{border-right:none}
  .cta{position:absolute;left:71px;top:1043px;font-family:"Roboto",sans-serif;font-weight:500;font-size:18px;color:#2a2a2a}
  .phone{position:absolute;left:452px;top:1032px;width:283px;height:44px;border-radius:22px;background:var(--pill);
    font-family:"Montserrat",sans-serif;font-weight:900;font-size:31px;color:#fff;text-align:center;line-height:44px}
  .footer{position:absolute;left:0;top:1094px;width:806px;height:46px;background:var(--footer-blue);
    font-family:"Montserrat",sans-serif;font-size:12px;letter-spacing:2.6px;color:#fff;text-align:center;line-height:46px}
</style>
</head>
<body>
<div class="flyer">
  <div class="tagline">Let <strong>VAULTLINE</strong> Take Care of your</div>
  <div class="subhead">SURVEILLANCE and IT HARDWARE NEEDS</div>
  <div class="brand-name"><span class="mark"></span>VAULTLINE</div>

  <svg class="hero" viewBox="0 0 806 370" role="img" aria-label="Photo of a glowing blue server room corridor with racks on both sides">
    <defs>
      <radialGradient id="heroGlow" cx="0.5" cy="0.45" r="0.7">
        <stop offset="0" stop-color="#cfeaff"/>
        <stop offset="0.25" stop-color="#3f8fd0"/>
        <stop offset="0.6" stop-color="#12345a"/>
        <stop offset="1" stop-color="#040c18"/>
      </radialGradient>
    </defs>
    <path d="M0 0 H472 Q481 0 481 9 V28 Q481 40 493 40 H806 V370 H0 Z" fill="url(#heroGlow)"/>
  </svg>

  <div class="intro">Due to the regulations put forth by the State of California, there is high cost associated with being in compliance to maintain your license and not receive fines as it pertains to security for your facility. In addition, the data intense programs with the seed-to-sale program can be a hindrance to you doing what you do best- running your business!</div>

  <div class="features left">
    <div class="feature">
      <svg class="icon" viewBox="0 0 22 22"><circle cx="11" cy="11" r="11" fill="var(--accent)"/><circle cx="11" cy="11" r="4" fill="none" stroke="#fff" stroke-width="1.5"/><circle cx="11" cy="11" r="1.3" fill="#fff"/></svg>
      <p><b>Experience</b>- we have been in the IT and video surveillance business for over 20 years</p>
    </div>
    <div class="feature">
      <svg class="icon" viewBox="0 0 22 22"><circle cx="11" cy="11" r="11" fill="var(--accent)"/><rect x="7" y="5.5" width="8" height="11" rx="1" fill="none" stroke="#fff" stroke-width="1.4"/><path d="M9 9h4M9 12h4" stroke="#fff" stroke-width="1.2"/></svg>
      <p><b>Compliance</b>- our attorney helped write Prop 64 and can keep you in compliance with the ever-changing regulations</p>
    </div>
    <div class="feature">
      <svg class="icon" viewBox="0 0 22 22"><circle cx="11" cy="11" r="11" fill="var(--accent)"/><path d="M7 15 L15 7 M8 8h2M12 14h2" stroke="#fff" stroke-width="1.6" stroke-linecap="round"/></svg>
      <p><b>Cost Savings</b>- Vaultline can save you 15-30% over the competition</p>
    </div>
    <div class="feature">
      <svg class="icon" viewBox="0 0 22 22"><circle cx="11" cy="11" r="11" fill="var(--accent)"/><path d="M6 13 L12 7 L12 11 L16 9 L10 15 L10 11 Z" fill="#fff"/></svg>
      <p><b>Speed</b>- our solutions can be designed and implemented within days, not months</p>
    </div>
  </div>

  <div class="features right">
    <div class="feature">
      <svg class="icon" viewBox="0 0 22 22"><circle cx="11" cy="11" r="11" fill="var(--accent)"/><circle cx="11" cy="11" r="4.5" fill="none" stroke="#fff" stroke-width="2" stroke-dasharray="2 1.5"/><circle cx="11" cy="11" r="1.5" fill="#fff"/></svg>
      <p><b>Customization</b>- our products are architected around the business not the business around the products</p>
    </div>
    <div class="feature">
      <svg class="icon" viewBox="0 0 22 22"><circle cx="11" cy="11" r="11" fill="var(--accent)"/><path d="M6 15h10M7 15v-3M10 15v-5M13 15v-7" stroke="#fff" stroke-width="1.6"/></svg>
      <p><b>Finance options</b>- Vaultline offers the following options for purchase</p>
    </div>
    <ul class="options">
      <li>Outright purchase- own your own equipment and data</li>
      <li>Leasing with a monthly payment- prevent large outlay of cash</li>
      <li>Managed/cloud offering- we send the gear and manage in a secure location</li>
    </ul>
  </div>

  <div class="offering-title">PRODUCT OFFERING</div>
  <div class="offering-bar">
    <span style="width:198px">Video Surveillance</span>
    <span style="width:137px">Data Storage</span>
    <span style="width:136px">Data Security</span>
    <span style="width:127px">Networking</span>
    <span style="width:208px">Wireless Connectivity</span>
  </div>

  <div class="cta">CALL US TODAY FOR A FREE CONSULTATION</div>
  <div class="phone">555-214-0386</div>

  <div class="footer">www.vaultlinesupply.com &nbsp;|&nbsp; info@vaultlinesupply.com</div>
</div>
</body>
</html>
```